Website Design Idea Only

I need a WordPress compatible website design idea. I have already hired a programmer, however; I am not happy with the design ideas he has come up with, I need help in creating a professional but classy/unique design for my company website.

A bit about my company....
Bid Compass (the logo was created here on ArtHarbor and I love it!!) is a brokerage company... I source out Print, Design and Websites for my customers, helping them find the best quality for the best prices, and saving them time and money by managing the project.
My company was called "M.P.R. Design & Printing", and you can view the current site at mprdesign-printing.example, but I am now operating as Bid Compass so I am needing an updated site.

What I would like to see in the site...
Because my site will be a big selling feature, I would like it to be professional, but some really nice/creative design characteristics to it. I am attaching what my programmer has come up with and you'll see it is very flat, and the pictures way to large. "Bid Compass-updated.jpg"
I am also attaching my logo, and a couple of site ideas I found that I like as well.

I was hoping for some sort of wave at the top, or something eye catching.
The design should say we are professional, but are creative and classy.
I love the gold/brown combination, as that is my logo, but I don't want a totally dark background, I like the use of whitespace as well.

Please feel free to contact my anytime if you have any questions, I will be happy to help!
Marta
marta@bidcompass.example

Please note: This design will proceed the design of two or three trade show pull up banners, which I am wanting to award to the winning designer. Please keep in mind that the graphics will need to be available in a vector format to accommodate that.

Thank you!!

Target Market(s)

Business to business - small to medium sized business.

Number of Pages Required

3 page

Requirements
Must have
• Please design a home page, a landing page that is specific to 'printing' or 'websites', as well as a 'regular' page.

```html
<!DOCTYPE html>
<html lang="en">
<head>
<meta charset="utf-8">
<title>Bid Compass – Home</title>
<link rel="stylesheet" href="https://fonts.googleapis.com/css2?family=Open+Sans:wght@400;600&display=swap">
<style>
  :root {
    --gold: #c08d4a;
    --gold-light: #dcc481;
    --gold-pale: #e8d79a;
    --gold-panel: #d3b46f;
    --gold-deep: #a87935;
    --ink: #1a1a1a;
    --charcoal: #242424;
    --header-dark: #2b2b2d;
    --black: #000;
    --white: #fff;
    --body-text: #3a3a3a;
    --ad-grey: #8c8c8c;
    --cream-text: #f0d995;
  }
  * { box-sizing: border-box; margin: 0; padding: 0; }
  html, body { width: 847px; height: 1200px; overflow: hidden; }
  body {
    position: relative;
    background: var(--white);
    font-family: "Open Sans", Arial, sans-serif;
    color: var(--body-text);
  }
  .abs { position: absolute; }

  /* Header */
  .site-header { left: 0; top: 0; width: 847px; height: 214px; background: var(--header-dark); overflow: hidden; }
  .site-header svg { position: absolute; left: 0; top: 0; }
  .brand { left: 76px; top: 40px; width: 180px; text-align: center; }
  .brand-mark { width: 44px; height: 44px; border-radius: 50%; border: 3px solid var(--gold); margin: 0 auto 10px; }
  .brand-name { font-size: 24px; font-weight: 600; color: var(--gold); letter-spacing: 1px; }
  .brand-tagline { font-size: 8px; color: var(--white); margin-top: 2px; }
  .header-phone { right: 31px; top: 20px; color: var(--gold-pale); font-size: 14px; display: flex; align-items: center; gap: 6px; }
  .main-nav { right: 32px; top: 83px; display: flex; gap: 20px; font-size: 11px; color: var(--gold-pale); }
  .search-field { left: 462px; top: 166px; width: 248px; height: 22px; background: var(--gold-pale); border: 2px solid var(--gold-deep); font-size: 11px; padding: 2px 8px; color: #333; }
  .search-go { left: 718px; top: 166px; width: 34px; height: 22px; background: var(--gold); font-size: 11px; text-align: center; line-height: 22px; color: #333; }

  /* Section bars */
  .section-bar { left: 20px; width: 569px; height: 40px; background: var(--gold); color: var(--white); font-size: 14px; padding-left: 19px; line-height: 40px; }

  /* Products */
  .product-panel { left: 20px; top: 302px; width: 569px; height: 252px; background: var(--gold-panel); }
  .product { top: 315px; width: 161px; }
  .product-image { height: 118px; }
  .product-name { margin-top: 9px; height: 21px; background: var(--black); color: var(--white); font-size: 10px; line-height: 21px; padding-left: 8px; }
  .product-text { margin-top: 7px; padding: 0 7px; font-size: 10.2px; line-height: 12.5px; color: #4a3a20; }

  /* Welcome */
  .welcome-text { left: 33px; top: 679px; width: 268px; font-size: 10.5px; line-height: 19px; color: var(--body-text); }
  .welcome-brand { left: 357px; top: 720px; width: 200px; text-align: center; }
  .welcome-brand .brand-mark { width: 56px; height: 56px; border-width: 4px; }
  .welcome-brand .brand-name { font-size: 26px; }

  /* Sidebar */
  .sidebar { left: 630px; top: 223px; width: 217px; height: 635px; background: var(--black); }
  .sidebar-title { font-size: 13px; color: var(--gold); }
  .sidebar-nav { left: 658px; top: 259px; }
  .sidebar-nav ul { list-style: none; margin: 14px 0 0 16px; font-size: 10px; color: var(--white); line-height: 19.2px; }
  .newsletter-panel { left: 630px; top: 440px; width: 217px; height: 167px; background: linear-gradient(160deg, var(--gold-pale), var(--gold-panel) 60%, #c9a85e); border: 3px solid var(--gold-deep); }
  .newsletter-panel .sidebar-title { position: absolute; left: 15px; top: 32px; color: #6b5630; }
  .field { background: var(--gold-pale); border: 2px solid var(--gold-deep); font-size: 10px; padding: 3px 8px; color: #333; height: 24px; }
  .button { background: linear-gradient(var(--gold-light), var(--gold-deep)); color: var(--ink); font-size: 10px; text-align: center; line-height: 26px; height: 26px; }
  .ad-slot { width: 84px; height: 84px; background: var(--ad-grey); color: #c7c7c7; font-size: 9.5px; text-align: center; display: flex; align-items: center; justify-content: center; line-height: 17px; }

  /* Footer */
  .footer-band { left: 0; top: 903px; width: 847px; height: 16px; background: var(--gold); }
  .footer { left: 0; top: 919px; width: 847px; height: 248px; background: var(--charcoal); }
  .footer-title { font-size: 13px; color: var(--gold); }
  .portfolio-grid { left: 58px; top: 978px; display: grid; grid-template-columns: repeat(3, 50px); gap: 6px; }
  .portfolio-grid div { height: 50px; }
  .footer-logo { left: 658px; top: 902px; width: 122px; height: 89px; background: var(--black); border: 4px solid var(--gold); text-align: center; padding-top: 14px; }
  .footer-logo .brand-mark { width: 26px; height: 26px; border-width: 2px; margin-bottom: 4px; }
  .footer-logo .brand-name { font-size: 13px; letter-spacing: 0; }
  .contact-list { left: 678px; top: 1025px; list-style: none; font-size: 10px; color: var(--cream-text); }
  .contact-list li { height: 27px; display: flex; align-items: center; gap: 14px; }
  .contact-list svg { width: 12px; height: 12px; fill: #9a9a9a; }
  .social-bar { left: 343px; top: 1105px; width: 196px; height: 31px; background: #2e2e2e; display: flex; align-items: center; justify-content: center; gap: 9px; }
  .social-bar span { width: 11px; height: 11px; border-radius: 50%; background: #6c6c6c; }
  .copyright-bar { left: 0; top: 1167px; width: 847px; height: 33px; background: linear-gradient(var(--gold-light), var(--gold)); }
  .copyright { left: 357px; top: 1167px; width: 170px; height: 14px; background: var(--gold-deep); font-size: 8px; color: var(--ink); text-align: center; line-height: 14px; }
</style>
</head>
<body>

<header class="site-header abs">
  <svg width="847" height="214" viewBox="0 0 847 214" aria-hidden="true">
    <defs>
      <linearGradient id="lowerSweep" x1="0" y1="0" x2="1" y2="0">
        <stop offset="0" stop-color="#3a3b3f"/>
        <stop offset="1" stop-color="#4e5258"/>
      </linearGradient>
    </defs>
    <rect width="847" height="6" fill="#c08d4a"/>
    <path d="M0 6 L847 6 L847 8 L0 8Z" fill="#1a1a1a"/>
    <path d="M300 6 L560 214 L600 214 L340 6Z" fill="#333437" opacity="0.6"/>
    <path d="M120 214 C330 185 520 110 847 150 L847 214Z" fill="url(#lowerSweep)"/>
    <path d="M180 186 C400 170 600 110 847 140" fill="none" stroke="#c08d4a" stroke-width="4"/>
    <path d="M8 12 L8 186 L40 186 L40 198 L300 198" fill="none" stroke="#c08d4a" stroke-width="3"/>
    <rect x="0" y="208" width="847" height="6" fill="#c08d4a"/>
  </svg>
  <div class="brand abs">
    <div class="brand-mark"></div>
    <div class="brand-name">BID COMPASS</div>
    <div class="brand-tagline">The Smart Way to Save Money</div>
  </div>
  <div class="header-phone abs">
    <svg width="14" height="14" viewBox="0 0 24 24" aria-hidden="true"><path fill="#fff" d="M6.6 10.8a15 15 0 0 0 6.6 6.6l2.2-2.2c.3-.3.7-.4 1-.2 1.1.4 2.3.6 3.6.6.6 0 1 .4 1 1V20c0 .6-.4 1-1 1A17 17 0 0 1 3 4c0-.6.4-1 1-1h3.5c.6 0 1 .4 1 1 0 1.3.2 2.5.6 3.6.1.3 0 .7-.2 1z"/></svg>
    1-888-555-0142
  </div>
  <nav class="main-nav abs">
    <span>Home</span><span>About Us</span><span>Services</span><span>Request Quote</span><span>Contact Info</span>
  </nav>
  <div class="search-field abs">Search</div>
  <div class="search-go abs">Go</div>
</header>

<div class="section-bar abs" style="top:253px">Featured Products</div>
<div class="product-panel abs"></div>

<div class="product abs" style="left:32px">
  <div class="product-image" role="img" aria-label="Illustration of a cup holding paint brushes" style="background:radial-gradient(circle at 55% 50%, #5a3d8f, #201540 75%)"></div>
  <div class="product-name">Product Name</div>
  <p class="product-text">we have developed that set M.P.R. apart, because we feel every project is important, and the lowest price and the best quality are just the</p>
</div>
<div class="product abs" style="left:219px">
  <div class="product-image" role="img" aria-label="Illustration of an easel holding a flower painting" style="background:radial-gradient(circle at 50% 45%, #3b4a78, #0d1020 75%)"></div>
  <div class="product-name">Product Name</div>
  <p class="product-text">we have developed that set M.P.R. apart, because we feel every project is important, and the lowest price and the best quality are just the</p>
</div>
<div class="product abs" style="left:406px">
  <div class="product-image" role="img" aria-label="Illustration of a photo frame with a flower picture" style="background:radial-gradient(circle at 50% 45%, #f4f4f4, #c9c9c9 80%)"></div>
  <div class="product-name">Product Name</div>
  <p class="product-text">we have developed that set M.P.R. apart, because we feel every project is important, and the lowest price and the best quality are just the</p>
</div>

<div class="section-bar abs" style="top:606px">Welcome to M.P.R. Design &amp; Printing</div>
<p class="welcome-text abs">Real Service, Real Value!<br>Customer focused service is how M.P.R. built its reputation. We take the time to understand our customer's true needs, and we do whatever it takes to meet, and often exceed, their expectations. It's the personal relationships that we have developed that set M.P.R. apart, because we feel every project is important, and the lowest price and the best quality are just the starting points for our relationship. We'll show you just what a professional brokerage can do for you!</p>
<div class="welcome-brand abs">
  <div class="brand-mark"></div>
  <div class="brand-name">BID COMPASS</div>
</div>

<aside class="sidebar abs"></aside>
<div class="sidebar-nav abs">
  <h3 class="sidebar-title" style="font-weight:400">Navigation</h3>
  <ul><li>Home</li><li>About Us</li><li>Services</li><li>Request Quote</li><li>Contact Info</li></ul>
</div>
<div class="newsletter-panel abs">
  <h3 class="sidebar-title" style="font-weight:400">Subscribe for Newsletter</h3>
</div>
<div class="field abs" style="left:644px;top:503px;width:188px">Email Address</div>
<div class="button abs" style="left:765px;top:545px;width:67px">Subscribe</div>

<div class="ad-slot abs" style="left:644px;top:634px">120 X 120<br>Ad Space</div>
<div class="ad-slot abs" style="left:744px;top:634px">120 X 120<br>Ad Space</div>
<div class="ad-slot abs" style="left:644px;top:744px">120 X 120<br>Ad Space</div>
<div class="ad-slot abs" style="left:744px;top:744px">120 X 120<br>Ad Space</div>

<div class="footer-band abs"></div>
<footer class="footer abs"></footer>

<h3 class="footer-title abs" style="left:58px;top:946px;font-weight:400">From Portfolio</h3>
<div class="portfolio-grid abs" role="img" aria-label="Grid of nine portfolio thumbnails">
  <div style="background:#8a8a8a"></div>
  <div style="background:linear-gradient(135deg,#c08a30,#5a3a10)"></div>
  <div style="background:linear-gradient(#1c2a44,#c06a2a)"></div>
  <div style="background:#c21c1c"></div>
  <div style="background:#4a4a4a"></div>
  <div style="background:linear-gradient(135deg,#d09a3a,#6a4410)"></div>
  <div style="background:linear-gradient(#2a3c6a,#d08a40)"></div>
  <div style="background:linear-gradient(135deg,#2e5aa0,#c04080)"></div>
  <div style="background:#9a9aa4"></div>
</div>

<h3 class="footer-title abs" style="left:336px;top:949px;font-weight:400">Subscribe for Newsletter</h3>
<div class="field abs" style="left:334px;top:999px;width:187px">Email Address</div>
<div class="button abs" style="left:454px;top:1040px;width:67px">Subscribe</div>

<div class="social-bar abs" aria-label="Social links">
  <span></span><span></span><span></span><span></span><span></span><span></span><span></span><span></span>
</div>

<div class="footer-logo abs">
  <div class="brand-mark"></div>
  <div class="brand-name">BID COMPASS</div>
</div>

<ul class="contact-list abs">
  <li><svg viewBox="0 0 24 24"><path d="M6.6 10.8a15 15 0 0 0 6.6 6.6l2.2-2.2c.3-.3.7-.4 1-.2 1.1.4 2.3.6 3.6.6.6 0 1 .4 1 1V20c0 .6-.4 1-1 1A17 17 0 0 1 3 4c0-.6.4-1 1-1h3.5c.6 0 1 .4 1 1 0 1.3.2 2.5.6 3.6.1.3 0 .7-.2 1z"/></svg>1-888-555-0142</li>
  <li><svg viewBox="0 0 24 24"><rect x="7" y="2" width="10" height="20" rx="2"/></svg>1-888-555-0142</li>
  <li><svg viewBox="0 0 24 24"><path d="M2 5h20v14H2z M2 5l10 8 10-8" /></svg>info@bidcompass.example</li>
  <li><svg viewBox="0 0 24 24"><circle cx="12" cy="12" r="10"/></svg>www.bidcompass.example</li>
</ul>

<div class="copyright-bar abs"></div>
<div class="copyright abs">© 2014 bidcompass.example  All rights reserved.</div>

</body>
</html>
```